Brantley & Co Flyer (tri-fold) Accounting Firm

We are an accounting firm that provides loan broking services. We would like the brochure to look sophisticated but not too formal.

We would like to add some background colour to the flyer/brochure (attached in word and PDF version) in the following green (Hex Colour #94c947) in different styles/patterns etc.

Guidelines:

• We envisage that the green would cover approximately 30% of the background

• Do not change any of the content

• Change fonts as required

• The wording, titles/headings and background can be a combination of the green colour #94c947, black and white.

• We are happy to use multiple shadings of the green colour above to give contrast and depth

• We would like a 3-5mm bleed around the edges.

• Please remove black page break lines are to disappear (not sure how to remove on word document).

• Please stretch all images to the edge of the bleed (except for KLVN, Ledgerline Planner, Homeward Select and EasyNest 480 logos).

• Please insert different icons for phone, fax and email, e.g. an image of a telephone next to our number instead of the symbol “P”.

We have included a copy of a business card as an example of our existing style we wish to retain in the brochure.

Please provide appropriate file types to enable publishing of brochures.

Target Market(s)

Business owners and individuals requiring accounting and services, people requiring loans/refinance, superannuation retirees

Industry/Entity Type

Accounting

Font styles to use
Other font styles liked:
• Refer to business card font

Colors
abd037

Requirements
Must have
• Must use our Brantley & Co logo green with black text (as in the attached brochure).
Nice to have
• The design concept does not need to necessarily include the KLVN, Ledgerline Planner, Homeward Select and EasyNest 480 logos, this may create a simpler cleaner look. I'd like to look at the brochure design with and without those additional logos for comparison purposes.

```html
<!DOCTYPE html>
<html lang="en">
<head>
<meta charset="utf-8">
<title>Brantley &amp; Co – Tri-fold Brochure</title>
<link href="https://fonts.googleapis.com/css2?family=Arimo:wght@400;700&display=swap" rel="stylesheet">
<style>
  :root{
    --green:#94c947;
    --green-dark:#7fb436;
    --green-light:#a9d562;
    --charcoal:#4a4b4d;
    --paper:#f2f2f2;
    --white:#ffffff;
    --ink:#1e1e1e;
    --grey-text:#b9b9b9;
  }
  *{margin:0;padding:0;box-sizing:border-box}
  html,body{width:1200px;height:855px;overflow:hidden;background:#dcdcdc}
  body{font-family:"Arimo",Arial,sans-serif;color:var(--white)}
  .brochure{position:relative;width:1200px;height:855px;display:flex}
  .panel{position:relative;width:400px;height:855px;overflow:hidden}

  /* ---------- shared name lockup ---------- */
  .brand-lockup{position:absolute;display:flex;align-items:center;gap:14px}
  .brand-dot{width:34px;height:34px;border-radius:50%;background:var(--green);flex:none}
  .brand-name{font-family:"Arimo",Arial,sans-serif;font-weight:400;font-size:30px;line-height:1;color:var(--green)}

  /* ---------- contact panel ---------- */
  .contact-panel{background:var(--charcoal)}
  .family-photo{position:absolute;left:0;top:0;width:400px;height:360px;
    background:linear-gradient(160deg,#e8ece4 0%,#c9c39a 35%,#9a8a5a 65%,#6d6a3e 100%)}
  .contact-shape{position:absolute;left:0;top:0}
  .location-map{position:absolute;left:60px;top:280px;width:220px;height:220px;border-radius:50%;
    background:linear-gradient(135deg,#ecebe6,#dcdad2);border:9px solid #9c9d9f}
  .contact-title{position:absolute;left:60px;top:540px;font-size:28px;font-weight:700;color:var(--green);letter-spacing:.5px}
  .contact-list{position:absolute;left:60px;top:590px;list-style:none;font-size:17px;line-height:1.25}
  .contact-list li{display:flex;align-items:flex-start;gap:10px;margin-bottom:14px}
  .contact-list svg{flex:none;margin-top:3px}
  .contact-panel .brand-lockup{left:60px;top:782px}

  /* ---------- origins panel ---------- */
  .origins-panel{background:linear-gradient(180deg,var(--green-light) 0%,var(--green) 45%,var(--green-dark) 100%);padding:60px 44px 0 44px}
  .origins-title{font-size:30px;font-weight:400;letter-spacing:.5px}
  .origins-sub{font-size:22px;font-weight:400;margin:4px 0 24px 60px}
  .origins-panel p{font-size:12.5px;line-height:1.35;margin-bottom:14px}
  .testimonials-title{font-size:20px;font-weight:400;text-align:center;margin:26px 0 16px}
  .testimonial-author{display:block;font-weight:700}

  /* ---------- cover panel ---------- */
  .cover-panel{background:var(--charcoal)}
  .cover-head{position:absolute;left:0;top:0;width:400px;height:180px;background:var(--paper)}
  .cover-panel .brand-lockup{left:0;top:72px;width:400px;justify-content:center}
  .cover-panel .brand-name{color:var(--ink);font-size:32px}
  .meeting-photo{position:absolute;left:0;top:180px;width:400px;height:260px;
    background:linear-gradient(135deg,#8a7d6a 0%,#6f6455 40%,#b8b2a6 70%,#5f5649 100%)}
  .cover-shape{position:absolute;left:0;top:0}
  .service-list{position:absolute;left:40px;top:480px;list-style:none;font-size:19px;color:var(--green);line-height:1.4}
  .service-list li{display:flex;align-items:center;gap:10px}
  .cover-cta{position:absolute;right:30px;top:588px;width:240px;text-align:right;font-size:10px;line-height:1.35}
  .web-band{position:absolute;left:60px;top:628px;width:340px;height:40px;background:var(--green);
    display:flex;align-items:center;padding-left:22px;font-size:21px;font-weight:700;color:var(--white)}
  .badges{position:absolute;left:60px;top:700px;width:310px;display:flex;justify-content:space-between;align-items:center}
  .badge{width:34px;height:34px;border-radius:50%;background:#6a6b6d}
  .principal{position:absolute;left:0;top:712px;width:400px;text-align:center;font-size:10px;color:var(--grey-text)}
</style>
</head>
<body>
<main class="brochure">

  <section class="panel contact-panel">
    <div class="family-photo" role="img" aria-label="Photo of a smiling family of grandparents and grandchildren in a grassy field"></div>
    <svg class="contact-shape" width="400" height="855" viewBox="0 0 400 855" aria-hidden="true">
      <path d="M0 390 C120 360 260 330 400 230 L400 855 L0 855 Z" fill="var(--green)"/>
      <path d="M0 402 C130 375 270 348 400 256 L400 855 L0 855 Z" fill="var(--charcoal)"/>
    </svg>
    <div class="location-map" role="img" aria-label="Street map showing the office location"></div>
    <h2 class="contact-title">CONTACT US</h2>
    <ul class="contact-list">
      <li><svg width="12" height="16" viewBox="0 0 12 16"><path d="M6 0a6 6 0 0 0-6 6c0 4.5 6 10 6 10s6-5.5 6-10a6 6 0 0 0-6-6zm0 8.5A2.5 2.5 0 1 1 6 3.5a2.5 2.5 0 0 1 0 5z" fill="var(--green)"/></svg><span>418 Harbour Road<br>Elmsfield SA 5099</span></li>
      <li><svg width="14" height="14" viewBox="0 0 14 14"><path d="M3 0l2.5 3.5-1.5 2a8 8 0 0 0 4.5 4.5l2-1.5L14 11l-2 3C5.5 14 0 8.5 0 2z" fill="var(--green)"/></svg><span>(08) 7100 4821</span></li>
      <li><svg width="14" height="11" viewBox="0 0 14 11"><rect width="14" height="11" fill="var(--green)"/><path d="M0 0l7 6 7-6" stroke="var(--charcoal)" stroke-width="1.4" fill="none"/></svg><span>admin@brantley-co.com.au</span></li>
      <li><svg width="14" height="14" viewBox="0 0 14 14"><circle cx="7" cy="7" r="6" stroke="var(--green)" stroke-width="1.5" fill="none"/><path d="M1 7h12M7 1c-3 3-3 9 0 12M7 1c3 3 3 9 0 12" stroke="var(--green)" stroke-width="1.2" fill="none"/></svg><span>brantley-co.com.au</span></li>
    </ul>
    <div class="brand-lockup">
      <span class="brand-dot"></span>
      <span class="brand-name">Brantley &amp; Co</span>
    </div>
  </section>

  <section class="panel origins-panel">
    <h1 class="origins-title">BRANTLEY &amp; CO</h1>
    <h2 class="origins-sub">Our Origins</h2>
    <p>The firm's origins were established in 1994 when Daniel Brantley commenced public practice in Seacliff Bay. In 2006, the firm relocated to Elmsfield as the client base grew.</p>
    <p>At Brantley &amp; Co, we understand that the world is constantly changing, however when it comes to values we believe some things should never change.</p>
    <p>Values such as trust, integrity and confidentiality are as fundamental to us in our business relationships as they are in our everyday lives.</p>
    <h2 class="testimonials-title">Client Testimonials</h2>
    <p>We have been a client of Brantley &amp; Co for twenty years and are very happy with their services. Brantley &amp; Co has been the perfect accounting firm for all our accounting needs, business advice and support. Dan and his team place customer satisfaction at the top of their agenda and back it up with all of the knowledge you could ever need. Any enquiry or concern is swiftly dealt with and the support is second to none.</p>
    <p>Over the years Brantley &amp; Co have been an important and stable part of our company and we will enjoy using their services in the future.<span class="testimonial-author">Trevor, Builder, Ridgeway</span></p>
    <p>Our newsagency was fortunate to be a client of Brantley &amp; Co for over 20 years. We received amazing support by Dan and his team during a particularly difficult personal time, the sale of our family business. When the sale was complete, considering all the time we were afforded, we were amazed at the very small amount we had to pay for their amazing support.<span class="testimonial-author">Louise, Seacliff Bay</span></p>
  </section>

  <section class="panel cover-panel">
    <div class="cover-head"></div>
    <div class="brand-lockup">
      <span class="brand-dot"></span>
      <span class="brand-name">Brantley &amp; Co</span>
    </div>
    <div class="meeting-photo" role="img" aria-label="Photo of a business meeting table with coffee cups, a tablet and printed charts"></div>
    <svg class="cover-shape" width="400" height="855" viewBox="0 0 400 855" aria-hidden="true">
      <path d="M0 420 C130 450 270 430 400 360 L400 855 L0 855 Z" fill="var(--charcoal)"/>
    </svg>
    <ul class="service-list">
      <li><svg width="14" height="11" viewBox="0 0 14 11"><path d="M1 5.5l4 4L13 1" stroke="var(--green)" stroke-width="2.4" fill="none"/></svg>Accounting and Taxation</li>
      <li><svg width="14" height="11" viewBox="0 0 14 11"><path d="M1 5.5l4 4L13 1" stroke="var(--green)" stroke-width="2.4" fill="none"/></svg>Mortgage and Finance</li>
      <li><svg width="14" height="11" viewBox="0 0 14 11"><path d="M1 5.5l4 4L13 1" stroke="var(--green)" stroke-width="2.4" fill="none"/></svg>Self Managed Super Funds</li>
    </ul>
    <p class="cover-cta">Contact us today to book a free appointment to discuss how we can assist you</p>
    <div class="web-band">www.brantley-co.com.au</div>
    <div class="badges"><span class="badge"></span><span class="badge"></span></div>
    <p class="principal">Principal: Daniel Brantley</p>
  </section>

</main>
</body>
</html>
```